Business Card Design Project : Tidewell Press

In preparation for market launch, Whistler's Tidewell Press require the development of a business card. Tidewell Press is a Community online publishing web portal. We provide the the city of Whistler located in B.C. (Canada) business directories, News, Classified ads, News, Events and blogs etc.

The main focus of the brand is to help local businesses to corporate with their online advertisement and marketing. Meeting our clients face to face is a must (B2B).

Target Market(s)

The target market is B2B customers. Business Owners to Marketing, advertising Managers

Industry/Entity Type

Business

Requirements
Must have
• - The business card will be two sided.
the BACK side will have our logo which consist of (icon, url,slogan) submited. The logo will be middle and centred.

The FRONT side should have company details:

Company Legal Name: FERNDALE TIDEWELL PRESS

Owen Marsk
Director of Sales & Marketing

www.ferndaletidewell.biz
owen@ferndaletidewell.biz

Phone: 555 014 3826
#2817 - 562 E. Harlow Ave.
Vancouver, B.C. K7P2R4 Canada
Nice to have
• - For the "FRONT" side of our business card. You can separate or re-arrange with our logo components (icon, logo,slogan). It does not have to be together.

Also our company legal name is rather long so arrange or organize the name in a way to make it shorter. Your experience and creativity will have to come in play.
Should not have
• should not have other colors beside logo color and black text (2 colors). Also nothing Three dimensional

```html
<!DOCTYPE html>
<html lang="en">
<head>
<meta charset="utf-8">
<title>Tidewell Press – Business Card</title>
<link rel="stylesheet" href="https://fonts.googleapis.com/css2?family=Cinzel:wght@400;500&family=Tinos&family=PT+Sans:wght@400;700&display=swap">
<style>
  :root {
    --brand-blue: #0a7fd4;
    --brand-blue-soft: #7fb9e8;
    --ink: #111111;
    --card-white: #ffffff;
    --label-red: #e0393e;
    --stage-dark: #000000;
    --stage-light: #c4c4c4;
  }
  * { margin: 0; padding: 0; box-sizing: border-box; }
  html, body { width: 1200px; height: 640px; overflow: hidden; }
  body {
    position: relative;
    background: linear-gradient(90deg, var(--stage-dark) 0%, #3a3a3a 40%, #8a8a8a 70%, var(--stage-light) 100%);
    font-family: "Tinos", serif;
  }
  .side-label {
    position: absolute;
    top: 104px;
    width: 300px;
    text-align: center;
    font-family: "PT Sans", sans-serif;
    font-size: 50px;
    color: var(--label-red);
    letter-spacing: 1px;
  }
  .side-label--front { left: 119px; }
  .side-label--back { left: 750px; }

  .card {
    position: absolute;
    top: 209px;
    height: 278px;
    background: var(--card-white);
    border: 3px solid var(--ink);
    overflow: hidden;
  }
  .card--front { left: 33px; width: 546px; }
  .card--back { left: 636px; width: 539px; }

  /* Front */
  .corner-accent {
    position: absolute;
    left: 0;
    bottom: 0;
    width: 126px;
    height: 100px;
    border-top-right-radius: 126px 100px;
    background: radial-gradient(circle at 30% 100%, var(--brand-blue-soft) 0%, var(--brand-blue) 75%);
  }
  .corner-name {
    position: absolute;
    top: 12px;
    right: 14px;
    display: flex;
    align-items: center;
    gap: 7px;
    font-family: "PT Sans", sans-serif;
    font-weight: 700;
    font-size: 19px;
    color: var(--brand-blue);
  }
  .corner-name .dot {
    width: 12px; height: 12px;
    border-radius: 50%;
    background: var(--brand-blue);
  }
  .contact {
    position: absolute;
    left: 18px;
    width: 526px;
    top: 48px;
    text-align: center;
    color: var(--ink);
  }
  .contact__company {
    font-family: "Cinzel", serif;
    font-weight: 400;
    font-size: 37px;
    letter-spacing: 2px;
    line-height: 40px;
  }
  .contact__person {
    font-family: "Cinzel", serif;
    font-size: 23px;
    letter-spacing: 1px;
    line-height: 26px;
    margin-top: 2px;
  }
  .contact__title { font-size: 11.5px; line-height: 13px; }
  .contact__line { font-size: 14px; line-height: 15px; }
  .contact__phone { font-size: 13.5px; margin-top: 8px; line-height: 16px; }
  .contact__address { font-size: 11.5px; line-height: 14px; margin-top: 6px; }

  /* Back */
  .back-lockup {
    position: absolute;
    inset: 0;
    display: flex;
    flex-direction: column;
    align-items: center;
    font-family: "PT Sans", sans-serif;
  }
  .back-lockup__name {
    margin-top: 62px;
    display: flex;
    align-items: center;
    gap: 14px;
    font-weight: 700;
    font-size: 50px;
    line-height: 60px;
    color: var(--brand-blue);
  }
  .back-lockup__name .dot {
    width: 28px; height: 28px;
    border-radius: 50%;
    background: var(--brand-blue);
  }
  .back-lockup__url {
    margin-top: 34px;
    font-weight: 700;
    font-size: 26px;
    color: var(--ink);
    line-height: 28px;
  }
  .back-lockup__slogan {
    font-size: 44px;
    color: var(--brand-blue);
    line-height: 48px;
  }
</style>
</head>
<body>
  <div class="side-label side-label--front">FRONT</div>
  <div class="side-label side-label--back">BACK</div>

  <section class="card card--front" aria-label="Business card front">
    <div class="corner-accent" role="img" aria-label="Blue decorative corner accent"></div>

    <div class="corner-name"><span class="dot"></span>Tidewell Press</div>

    <div class="contact">
      <h1 class="contact__company">F. T. Press</h1>
      <p class="contact__person">Owen Marsk</p>
      <p class="contact__title">Director of Sales &amp; Marketing</p>
      <p class="contact__line">owen@ferndaletidewell.biz</p>
      <p class="contact__line">www.ferndaletidewell.biz</p>
      <p class="contact__phone">Phone: 555 014 3826</p>
      <p class="contact__address">#2817 - 562 E. Harlow Ave.<br>Vancouver, B.C. K7P2R4 Canada</p>
    </div>
  </section>

  <section class="card card--back" aria-label="Business card back">
    <div class="back-lockup">
      <div class="back-lockup__name"><span class="dot"></span>Tidewell Press</div>
      <p class="back-lockup__url">www.ferndaletidewell.biz</p>
      <p class="back-lockup__slogan">Your information gateway</p>
    </div>
  </section>
</body>
</html>
```